" Atendemos de maneira integrada em reabilitação ,tanto odontológica como neurológica. Somos terapia ocupacional, fonoaudiologia, neuropediatria e odontologia. Trabalhamos com técnicas de ponta e muito proximidade com nossos pacientes e suas famílias. "

```html
<!DOCTYPE html>
<html lang="pt-BR">
<head>
<meta charset="utf-8">
<title>Vitalis Integra – assinatura de e-mail</title>
<link rel="stylesheet" href="https://fonts.googleapis.com/css2?family=Montserrat:wght@700&family=Open+Sans:wght@400;600&display=swap">
<style>
  :root{
    --page:#ffffff;
    --navy:#0f3866;
    --blue:#1f5f9a;
    --mark-green:#8cc48a;
    --mark-blue:#2a86c4;
    --ink-light:#ffffff;
  }
  html,body{margin:0;padding:0;overflow:hidden;}
  body{width:1200px;height:1200px;background:var(--page);position:relative;font-family:"Open Sans",sans-serif;}
  .signature{position:absolute;left:163px;top:482px;width:850px;height:204px;}
  .signature-bg{position:absolute;inset:0;}
  .brand-emblem{position:absolute;left:0;top:0;width:240px;height:204px;}
  .brand{position:absolute;left:315px;top:40px;width:170px;text-align:center;color:var(--ink-light);}
  .brand-dot{display:block;width:44px;height:44px;margin:0 auto 14px;border-radius:50%;background:var(--mark-blue);}
  .brand-name{font-family:"Montserrat",sans-serif;font-weight:700;font-size:21px;letter-spacing:.5px;line-height:1;margin:0;}
  .brand-team{font-size:10.5px;line-height:1;margin:5px 0 0;white-space:nowrap;}
  .contact{position:absolute;right:48px;top:60px;margin:0;padding:0;list-style:none;color:var(--ink-light);font-size:15.5px;line-height:26.5px;text-align:right;}
  .contact li{display:flex;justify-content:flex-end;align-items:center;gap:10px;}
  .contact svg{width:13px;height:13px;flex:none;}
  .social-square{width:11px;height:11px;background:var(--ink-light);flex:none;margin:0 1px;}
  .contact .no-icon{padding-right:23px;}
</style>
</head>
<body>
  <section class="signature">
    <svg class="signature-bg" viewBox="0 0 850 204" preserveAspectRatio="none" aria-hidden="true">
      <defs>
        <linearGradient id="panelGrad" x1="0" y1="0" x2="1" y2="0">
          <stop offset="0" stop-color="#0d3260"/>
          <stop offset="1" stop-color="#1f5f9a"/>
        </linearGradient>
      </defs>
      <path d="M270 0 H850 V204 H180 C240 150 275 80 270 0 Z" fill="url(#panelGrad)"/>
    </svg>
    <svg class="brand-emblem" viewBox="0 0 240 204" role="img" aria-label="Símbolo da clínica Vitalis Integra">
      <defs>
        <linearGradient id="emblemGrad" x1="0" y1="0" x2="1" y2="1">
          <stop offset="0" stop-color="#8cc48a"/>
          <stop offset="1" stop-color="#2a86c4"/>
        </linearGradient>
      </defs>
      <circle cx="125" cy="100" r="92" fill="url(#emblemGrad)" opacity=".35"/>
    </svg>
    <div class="brand">
      <span class="brand-dot"></span>
      <p class="brand-name">VITALIS INTEGRA</p>
      <p class="brand-team">Paulo Andrade &amp; Helena Costa</p>
    </div>
    <ul class="contact">
      <li>vitalisintegra <span class="social-square"></span></li>
      <li>contato@exemplo.com
        <svg viewBox="0 0 16 16"><rect x="1" y="3" width="14" height="10" fill="#fff"/><path d="M1 3 L8 9 L15 3" fill="none" stroke="#1a4f85" stroke-width="1.5"/></svg>
      </li>
      <li>(00)0000-0000
        <svg viewBox="0 0 16 16"><path d="M3 1 L6 1 L7 5 L5 6.5 C6 9 7 10 9.5 11 L11 9 L15 10 L15 13 C15 14 14 15 13 15 C6 15 1 10 1 3 C1 2 2 1 3 1 Z" fill="#fff"/></svg>
      </li>
      <li>rua sem nome,00 Bairro Sem Nome
        <svg viewBox="0 0 16 16"><path d="M8 1 C4.7 1 3 3.4 3 6 C3 9.5 8 15 8 15 C8 15 13 9.5 13 6 C13 3.4 11.3 1 8 1 Z" fill="#fff"/><circle cx="8" cy="6" r="2" fill="#1a4f85"/></svg>
      </li>
      <li class="no-icon">Cidade Sem Nome</li>
    </ul>
  </section>
</body>
</html>
```